Webdesign für Zahnarztpraxis
Zielgruppe
Zahnarztpraxis
Aufgabenstellung
- Klares und übersichtliches Desgin
- Nicht zu verspielt
- Informativ
- Leichte Naviagtion
- Das Design der alten Webseite soll NICHT kopiert werden
- Die Farben Blau und Grün aus dem Logo sollen sich wiederfinden
- Designbeispiele, die dem Kunden gefallen sind https://www.kolbeck-mirowski-zahnarztpraxis.de/ und https://www.praxisolwing.de/

```html
<!DOCTYPE html>
<html lang="de">
<head>
<meta charset="utf-8">
<title>Lindenzahn – Zahnarztpraxis</title>
<link rel="stylesheet" href="https://fonts.googleapis.com/css2?family=Heebo:wght@400;500;600&family=Poppins:wght@400;500&display=swap">
<style>
:root{
  --blue:#2a96d6;
  --green:#6cb12f;
  --ink:#1d1d1d;
  --muted:#3a3a3a;
  --gray:#f3f3f3;
  --white:#fff;
}
*{box-sizing:border-box;margin:0;padding:0}
html,body{width:1200px;height:4322px;overflow:hidden}
body{position:relative;background:var(--white);font-family:"Poppins",sans-serif;color:var(--ink)}
.abs{position:absolute}
h1,h2,h3,.heading{font-family:"Heebo",sans-serif;font-weight:500}
.blue{color:var(--blue)}.green{color:var(--green)}
.btn{position:absolute;display:flex;align-items:center;justify-content:center;border-radius:20px;font-size:11.5px;font-family:"Heebo",sans-serif;font-weight:500;height:28px;padding:0 20px;white-space:nowrap}
.btn-green{background:var(--green);color:#fff}
.btn-outline{background:#fff;border:1.5px solid var(--green);color:var(--ink)}
.btn-outline-blue{background:#fff;border:1.5px solid var(--blue);color:var(--ink)}
.photo{position:absolute;border-radius:12px}
.body-text{font-size:10.5px;line-height:1.55;color:var(--muted)}

/* nav */
.nav-logo{left:151px;top:18px;font-family:"Heebo",sans-serif;font-weight:600;font-size:22px;color:var(--blue);display:flex;align-items:center;gap:8px}
.nav-logo i{display:block;width:18px;height:18px;border-radius:50%;background:var(--blue)}
.nav-links{left:360px;top:24px;display:flex;gap:34px;font-size:12px}
.nav-phone{left:918px;top:16px;width:132px;height:32px;background:var(--blue);color:#fff;border-radius:18px;font-size:12px;font-weight:500;display:flex;align-items:center;justify-content:center;gap:8px}

/* hero */
.hero-panel{left:25px;top:64px;width:562px;height:523px;border-radius:14px;background:linear-gradient(135deg,#f2f2f2,#fafafa)}
.hero-title{left:151px;top:222px;font-size:44px;line-height:1.16;font-weight:500}
.hero-sub{left:151px;top:340px;font-size:12px;line-height:1.45;width:345px}
.hero-photo{left:601px;top:64px;width:574px;height:540px;border-radius:14px;background:linear-gradient(160deg,#6d8a4e,#c7d6b8 45%,#eef2f5 80%)}

/* info band */
.band{left:62px;top:570px;width:1076px;height:254px;border-radius:16px;background:var(--blue);overflow:hidden;color:#fff}
.band h2{position:absolute;left:88px;top:72px;font-size:30px;line-height:1.25}
.band .greet{position:absolute;left:361px;top:58px;font-size:13px}
.pill{position:absolute;left:361px;height:28px;border-radius:15px;display:flex;align-items:center;padding:0 17px;font-size:11px}
.pill-green{background:var(--green)}
.pill-line{border:1.3px solid rgba(255,255,255,.85)}

/* section headings */
.sec-title{font-size:38px;font-weight:500}

/* cards */
.services{left:0;top:1337px;width:1200px;height:953px;background:var(--gray)}
.card{position:absolute;width:287px;height:322px;background:#fff;border-radius:12px}
.card .ico{position:absolute;left:40px;top:34px;width:62px;height:62px;border-radius:50%;background:var(--blue);display:flex;align-items:center;justify-content:center}
.card h3{position:absolute;left:40px;top:155px;font-size:17px;line-height:1.25;width:240px}
.card p{position:absolute;left:40px;width:210px;font-size:9.5px;line-height:1.5;color:var(--muted)}
.card .btn{left:40px;height:26px;font-size:11px}

/* team */
.member{position:absolute;width:287px}
.member .pic{height:302px;border-radius:10px;background:linear-gradient(170deg,#c9d6b4,#eef0ec 55%,#f8f8f8)}
.member .name{position:absolute;left:6px;top:322px;font-family:"Heebo",sans-serif;font-size:18px;line-height:1.2;width:230px}
.member .go{position:absolute;right:0;top:325px;width:29px;height:29px;border-radius:50%;background:var(--blue);display:flex;align-items:center;justify-content:center}

/* contact */
.contact{left:0;top:3418px;width:1200px;height:524px;background:var(--gray)}
.c-item{position:absolute;left:155px;display:flex;align-items:center;gap:18px;font-family:"Heebo",sans-serif;font-weight:500;font-size:15px;line-height:1.2}
.c-item .ring{width:40px;height:40px;border-radius:50%;border:1px solid #cfe3c1;background:#fff;display:flex;align-items:center;justify-content:center}
.hours{left:591px;top:3495px;width:458px;height:395px;background:#fff;border-radius:14px}
.hours h3{position:absolute;top:40px;font-size:20px}
.hours .row{position:absolute;font-size:11px;color:var(--muted)}

/* footer */
.footer{left:0;top:3942px;width:1200px;height:380px;background:var(--blue);color:#fff}
.footer h4{position:absolute;top:72px;font-family:"Heebo",sans-serif;font-weight:500;font-size:16px}
.footer ul{position:absolute;top:106px;list-style:none;font-size:11px;line-height:24px;color:rgba(255,255,255,.85)}
.foot-logo{left:151px;top:76px;font-family:"Heebo",sans-serif;font-weight:600;font-size:36px;display:flex;align-items:center;gap:12px}
.foot-logo i{width:28px;height:28px;border-radius:50%;background:#fff;display:block}
</style>
</head>
<body>

<!-- navigation -->
<div class="abs nav-logo"><i></i>Lindenzahn</div>
<nav class="abs nav-links"><span>Heim</span><span>Unsere Praxis</span><span>Dienstleistungen</span><span>Labor</span><span>Team</span><span>Kontakt</span></nav>
<div class="abs nav-phone">
  <svg width="13" height="13" viewBox="0 0 24 24" fill="none" stroke="#fff" stroke-width="2"><path d="M22 16.9v3a2 2 0 0 1-2.2 2 19.8 19.8 0 0 1-8.6-3.1 19.5 19.5 0 0 1-6-6A19.8 19.8 0 0 1 2.1 4.2 2 2 0 0 1 4.1 2h3a2 2 0 0 1 2 1.7c.1 1 .4 1.9.7 2.8a2 2 0 0 1-.5 2.1L8 9.9a16 16 0 0 0 6 6l1.3-1.3a2 2 0 0 1 2.1-.4c.9.3 1.8.6 2.8.7a2 2 0 0 1 1.7 2z"/></svg>
  49370011240
</div>

<!-- hero -->
<div class="abs hero-panel"></div>
<h1 class="abs hero-title"><span class="blue">Ihr Lächeln Ist</span> <span class="green">Unsere</span><br><span class="blue">Leidenschaft</span></h1>
<p class="abs hero-sub">Moderne Zahnmedizin in Sonnenfeld – persönlich, kompetent und fürsorglich.</p>
<div class="btn btn-green" style="left:151px;top:402px">Termin Vereinbaren</div>
<div class="btn btn-outline-blue" style="left:309px;top:402px">Leistungen Ansehen</div>
<div class="abs hero-photo" role="img" aria-label="Gruppenfoto des Praxisteams in weißer Kleidung im Garten"></div>

<!-- notice band -->
<section class="abs band">
  <h2>Wichtige<br>Information Für<br>Unsere Patienten</h2>
  <div class="greet">Liebe Patienten,</div>
  <div class="pill pill-green" style="top:90px">In der Zeit von xx.xx.2025 bis xx.xx.2025 bleibt unsere Praxis geschlossen.</div>
  <div class="pill pill-line" style="top:130px">Die Vertretung in dieser Zeit übernimmt Frau/Herr [Name].</div>
  <div class="pill pill-line" style="top:170px">Bitte melden Sie sich im Vorfeld telefonisch an.</div>
</section>

<!-- practice -->
<div class="photo" style="left:151px;top:911px;width:383px;height:339px;background:linear-gradient(160deg,#e9ecea,#fafafa 50%,#d9dcda)" role="img" aria-label="Heller Behandlungsraum mit Zahnarztstuhl und Fenster"></div>
<h2 class="abs sec-title blue" style="left:582px;top:994px">Unsere Praxis</h2>
<p class="abs body-text" style="left:582px;top:1056px;width:320px">Praxis &amp; Dentallabor In Sonnenfeld.<br>&nbsp;Prävention Und Individualprophylaxe In Jeder Altersgruppe!<br>&nbsp;Unsere Zahnärztin Spricht Auch Fließend Englisch</p>
<div class="btn btn-green" style="left:582px;top:1128px">Mehr Über Unsere Praxis</div>
<div class="abs" style="left:902px;top:884px;width:220px;height:220px;border-radius:50%;background:linear-gradient(150deg,#e8dfbf,#f4ede0)" role="img" aria-label="Zahnärztin bei der Behandlung eines Kindes"></div>
<div class="abs" style="left:903px;top:1026px;width:146px;height:150px;border-radius:50%;border:5px solid #fff;background:linear-gradient(160deg,#e6e3dc,#9c5a6a)" role="img" aria-label="Empfangsbereich mit Blumenschmuck"></div>

<!-- services -->
<section class="abs services">
  <h2 class="abs sec-title" style="left:151px;top:68px"><span class="blue">Was Wir</span> <span class="green">Anbieten</span></h2>
  <p class="abs body-text" style="left:151px;top:127px;width:500px;font-size:9.5px">Lorem Ipsum Dolor Sit Amet Consectetur. Fames Arcu Lacus Vel Duis Sed Facilisi Mattis. Integer Sed Euismod Semper Integer Arcu. Porttitor Turpis Cras Eget Sit Ut.</p>
  <div class="btn btn-green" style="left:896px;top:103px">Alle Dienste Anzeigen</div>
</section>

<!-- cards -->
<div class="card" style="left:151px;top:1549px">
  <div class="ico"><svg width="26" height="26" viewBox="0 0 24 24" fill="#fff"><path d="M7 3c-2.5 0-4 2-4 4.5 0 2 1 3.5 1.5 5 .5 2 .8 8.5 2.5 8.5 1.5 0 1.5-5 3-5h4c1.5 0 1.5 5 3 5 1.7 0 2-6.5 2.5-8.5.5-1.5 1.5-3 1.5-5C21 5 19.5 3 17 3c-2 0-3 1-5 1S9 3 7 3z"/></svg></div>
  <h3>Zahnärztliche Diagnostik</h3>
  <p style="top:193px">Lorem Ipsum Dolor Sit Amet Purus Nunc Vel Adipiscing Fringilla Nunc Eu Egestas Molestie. Ante Egestas.</p>
  <div class="btn btn-outline" style="top:260px">Jetzt Buchen</div>
</div>
<div class="card" style="left:456px;top:1549px">
  <div class="ico"><svg width="26" height="26" viewBox="0 0 24 24" fill="#fff"><path d="M7 3c-2.5 0-4 2-4 4.5 0 2 1 3.5 1.5 5 .5 2 .8 8.5 2.5 8.5 1.5 0 1.5-5 3-5h4c1.5 0 1.5 5 3 5 1.7 0 2-6.5 2.5-8.5.5-1.5 1.5-3 1.5-5C21 5 19.5 3 17 3c-2 0-3 1-5 1S9 3 7 3z"/></svg></div>
  <h3>Individualprophylaxe</h3>
  <p style="top:193px">Lorem Ipsum Dolor Sit Amet Purus Nunc Vel Adipiscing Fringilla Nunc Eu Egestas Molestie. Ante Egestas.</p>
  <div class="btn btn-green" style="top:260px">Jetzt Buchen</div>
</div>
<div class="card" style="left:763px;top:1549px">
  <div class="ico"><svg width="26" height="26" viewBox="0 0 24 24" fill="#fff"><path d="M7 3c-2.5 0-4 2-4 4.5 0 2 1 3.5 1.5 5 .5 2 .8 8.5 2.5 8.5 1.5 0 1.5-5 3-5h4c1.5 0 1.5 5 3 5 1.7 0 2-6.5 2.5-8.5.5-1.5 1.5-3 1.5-5C21 5 19.5 3 17 3c-2 0-3 1-5 1S9 3 7 3z"/></svg></div>
  <h3>Professionelle Zahnreinigung</h3>
  <p style="top:193px">Lorem Ipsum Dolor Sit Amet Purus Nunc Vel Adipiscing Fringilla Nunc Eu Egestas Molestie. Ante Egestas.</p>
  <div class="btn btn-outline" style="top:260px">Jetzt Buchen</div>
</div>
<div class="card" style="left:151px;top:1891px">
  <div class="ico"><svg width="26" height="26" viewBox="0 0 24 24" fill="#fff"><path d="M7 3c-2.5 0-4 2-4 4.5 0 2 1 3.5 1.5 5 .5 2 .8 8.5 2.5 8.5 1.5 0 1.5-5 3-5h4c1.5 0 1.5 5 3 5 1.7 0 2-6.5 2.5-8.5.5-1.5 1.5-3 1.5-5C21 5 19.5 3 17 3c-2 0-3 1-5 1S9 3 7 3z"/></svg></div>
  <h3>Konservierende<br>Zahnheilkunde</h3>
  <p style="top:214px">Lorem Ipsum Dolor Sit Amet Purus Nunc Vel Adipiscing Fringilla Nunc.</p>
  <div class="btn btn-outline" style="top:265px">Jetzt Buchen</div>
</div>
<div class="card" style="left:456px;top:1891px">
  <div class="ico"><svg width="26" height="26" viewBox="0 0 24 24" fill="#fff"><path d="M7 3c-2.5 0-4 2-4 4.5 0 2 1 3.5 1.5 5 .5 2 .8 8.5 2.5 8.5 1.5 0 1.5-5 3-5h4c1.5 0 1.5 5 3 5 1.7 0 2-6.5 2.5-8.5.5-1.5 1.5-3 1.5-5C21 5 19.5 3 17 3c-2 0-3 1-5 1S9 3 7 3z"/></svg></div>
  <h3>Zahnärztliche Prothetik</h3>
  <p style="top:193px">Lorem Ipsum Dolor Sit Amet Purus Nunc Vel Adipiscing Fringilla Nunc Eu Egestas Molestie. Ante Egestas.</p>
  <div class="btn btn-outline" style="top:260px">Jetzt Buchen</div>
</div>
<div class="card" style="left:763px;top:1891px">
  <div class="ico"><svg width="26" height="26" viewBox="0 0 24 24" fill="#fff"><path d="M7 3c-2.5 0-4 2-4 4.5 0 2 1 3.5 1.5 5 .5 2 .8 8.5 2.5 8.5 1.5 0 1.5-5 3-5h4c1.5 0 1.5 5 3 5 1.7 0 2-6.5 2.5-8.5.5-1.5 1.5-3 1.5-5C21 5 19.5 3 17 3c-2 0-3 1-5 1S9 3 7 3z"/></svg></div>
  <h3>Ästhetische Zahnheilkunde</h3>
  <p style="top:193px">Lorem Ipsum Dolor Sit Amet Purus Nunc Vel Adipiscing Fringilla Nunc Eu Egestas Molestie. Ante Egestas.</p>
  <div class="btn btn-outline" style="top:260px">Jetzt Buchen</div>
</div>

<!-- lab -->
<div class="abs" style="left:64px;top:2358px;width:220px;height:220px;border-radius:50%;background:linear-gradient(150deg,#efe4c4,#d7e3ee)" role="img" aria-label="Behandlung mit Mundschutz am Patienten"></div>
<div class="abs" style="left:140px;top:2500px;width:146px;height:146px;border-radius:50%;border:5px solid #fff;background:linear-gradient(150deg,#f1ece6,#e6cfc2)" role="img" aria-label="Zahntechnikerin bei der Arbeit im Labor"></div>
<h2 class="abs sec-title blue" style="left:314px;top:2468px">Praxislabor</h2>
<p class="abs body-text" style="left:314px;top:2530px;width:300px;font-size:9.5px">Unsere Praxis Verfügt Über Ein Eigenes Praxislabor – Für Höchste Präzision Und Schnelle Ergebnisse.</p>
<div class="btn btn-green" style="left:314px;top:2588px">Mehr Zum Praxislabor</div>
<div class="photo" style="left:666px;top:2379px;width:384px;height:339px;background:linear-gradient(160deg,#eef0f2,#fafafa 45%,#5b6877 47%,#f0e9df 70%)" role="img" aria-label="Moderner Behandlungsraum mit blauer Wand"></div>

<!-- team -->
<h2 class="abs sec-title" style="left:0;width:1200px;text-align:center;top:2790px"><span class="blue">Unser</span> <span class="green">Praxisteam</span></h2>
<p class="abs body-text" style="left:0;width:1200px;text-align:center;top:2847px;font-size:10px">Kompetent, Herzlich Und Darauf Fokussiert, Ihre Zahngesundheit Bestmöglich Zu Unterstützen.</p>
<div class="member" style="left:151px;top:2906px">
  <div class="pic" role="img" aria-label="Porträt der Assistentin"></div>
  <div class="name">Assistentin Lena Korbach</div>
  <div class="go"><svg width="11" height="11" viewBox="0 0 12 12" stroke="#fff" stroke-width="1.6" fill="none"><path d="M3 9l6-6M4 3h5v5"/></svg></div>
</div>
<div class="member" style="left:456px;top:2906px">
  <div class="pic" role="img" aria-label="Porträt der Zahnärztin"></div>
  <div class="name">Zahnärztin Ina Kessel</div>
  <div class="go"><svg width="11" height="11" viewBox="0 0 12 12" stroke="#fff" stroke-width="1.6" fill="none"><path d="M3 9l6-6M4 3h5v5"/></svg></div>
</div>
<div class="member" style="left:763px;top:2906px">
  <div class="pic" role="img" aria-label="Porträt der Zahntechnikerin"></div>
  <div class="name" style="top:312px">Zahntechnikerin Sabine Leuthold</div>
  <div class="go"><svg width="11" height="11" viewBox="0 0 12 12" stroke="#fff" stroke-width="1.6" fill="none"><path d="M3 9l6-6M4 3h5v5"/></svg></div>
</div>
<div class="btn btn-green" style="left:528px;top:3308px;width:144px">Alle TEAM Anzeigen</div>

<!-- contact -->
<section class="abs contact">
  <h2 class="abs sec-title blue" style="left:155px;top:118px">So Erreichen Sie Uns:</h2>
  <p class="abs body-text" style="left:155px;top:184px;width:300px;font-size:9.5px">Lorem Ipsum Dolor Sit Amet Consectetur. Ut Quis Quisque Imperdiet Volutpat Ac Vestibulum Lectus Nunc.</p>
  <div class="c-item" style="top:243px"><span class="ring"><svg width="14" height="14" viewBox="0 0 24 24" fill="var(--green)"><path d="M6.6 10.8a15 15 0 0 0 6.6 6.6l2.2-2.2a1 1 0 0 1 1-.2 11.4 11.4 0 0 0 3.6.6 1 1 0 0 1 1 1V20a1 1 0 0 1-1 1A17 17 0 0 1 3 4a1 1 0 0 1 1-1h3.5a1 1 0 0 1 1 1c0 1.3.2 2.5.6 3.6a1 1 0 0 1-.3 1z"/></svg></span><span>03701-12400<br>03701-12455</span></div>
  <div class="c-item" style="top:305px"><span class="ring"><svg width="14" height="14" viewBox="0 0 24 24" fill="var(--green)"><path d="M2 5h20v14H2z"/><path d="M2 5l10 8 10-8" stroke="#fff" stroke-width="2" fill="none"/></svg></span><span>Info@Zahnarztpraxis-Kessel.De</span></div>
  <div class="c-item" style="top:360px"><span class="ring"><svg width="14" height="14" viewBox="0 0 24 24" fill="var(--green)"><path d="M12 2a7 7 0 0 0-7 7c0 5 7 13 7 13s7-8 7-13a7 7 0 0 0-7-7zm0 9.5a2.5 2.5 0 1 1 0-5 2.5 2.5 0 0 1 0 5z"/></svg></span><span>Lindenweg 14<br>09100 Sonnenfeld</span></div>
</section>
<div class="abs hours">
  <h3 style="left:40px">Opening Hours:</h3>
  <h3 style="left:265px">Telefonzeiten:</h3>
  <div class="row" style="left:40px;top:90px">Montag: 9:00–13:00 &amp; 14:00–19:00</div>
  <div class="row" style="left:40px;top:118px">Dienstag: 9:00–13:00 &amp; 14:00–19:00</div>
  <div class="row" style="left:40px;top:146px">Mittwoch: 9:00–14:00</div>
  <div class="row" style="left:40px;top:174px">Donnerstag: Geschlossen</div>
  <div class="row" style="left:40px;top:202px">Freitag: 9:00–13:00</div>
  <div class="row" style="left:40px;top:230px">… Und Nach Vereinbarung</div>
  <div class="row" style="left:265px;top:90px">Montag: 9:00–15:00</div>
  <div class="row" style="left:265px;top:118px">Dienstag: 9:00–15:00</div>
  <div class="row" style="left:265px;top:146px">Mittwoch: 9:00–12:00</div>
  <div class="row" style="left:40px;top:268px;width:320px;line-height:1.5">In Dringenden Fällen Wenden Sie Sich Bitte An Den Zahnärztlichen Notdienst:</div>
  <div class="btn btn-green" style="left:40px;top:315px;height:26px">Zur Notdienstsuche</div>
</div>

<!-- footer -->
<footer class="abs footer">
  <div class="abs foot-logo"><i></i>Lindenzahn</div>
  <p class="abs" style="left:151px;top:172px;width:310px;font-size:10.5px;line-height:1.55;color:rgba(255,255,255,.85)">Praxis &amp; Dentallabor In Sonnenfeld.<br>&nbsp;Prävention Und Individualprophylaxe In Jeder Altersgruppe! Unsere Zahnärztin Spricht Auch Fließend Englisch</p>
  <h4 style="left:521px">Links</h4>
  <ul style="left:521px"><li>Home</li><li>About Us</li><li>Features</li><li>Pricing</li><li>Testimonials</li><li>Contact</li></ul>
  <h4 style="left:652px">Dienstleistungen</h4>
  <ul style="left:652px"><li>Zahnärztliche Diagnostik</li><li>Individualprophylaxe</li><li>Professionelle Zahnreinigung</li><li>Konservierende Zahnheilkunde</li><li>Zahnärztliche Prothetik</li></ul>
  <h4 style="left:873px">Kontaktieren Sie Uns</h4>
  <div class="abs" style="left:873px;top:108px;font-size:11px;line-height:16px;color:rgba(255,255,255,.85)">03701-12400<br>03701-12455<br><br>Info@Zahnarztpraxis-Kessel.De<br><br>Lindenweg 14<br>09100 Sonnenfeld</div>
  <div class="abs" style="left:151px;top:356px;font-size:8.5px;color:rgba(255,255,255,.85)">©2025 Zahnarztpraxis . All Rights Reserved</div>
  <div class="abs" style="left:926px;top:356px;font-size:8.5px;color:rgba(255,255,255,.85)">Privacy Policy &amp; Terms Of Use</div>
</footer>

</body>
</html>
```